Environmental and Industrial Services Company Needs Brochure Design

We need a new brochure design for an established company that services the Southeastern United States. It is a highly diversified company that centers around Environmental and Industrial Services. The Environmental side revolved around emergency chemical and spill response, HAZMAT, hazardous/ non hazardous waste management, wastewater treatment, and remediation services (cleaning up contaminated sites). And the Industrial side utilizes heavy equipment like vacuum trucks and hydroblasters to clean process equipment inside of factories and manufacturing facilities. Predominantly our clients are large industrial clients, commercial clients, and the government. The people who would see the brochure are decision makers; engineers, project managers, procurement heads for large companies. These are serious and educated people who are looking for the best.

The designs should incorporate our colors and I welcome you to use any of the pictures from our website www.kvlterra.com EXCLUSIVELY FOR THIS PROJECT, of course. This brochure should communicate professionalism, confidence, stability, and portray the kind of company who efficiently manages complicated issues. Our site gives a better kind of idea of the branding we want to extend into the brochure and I caution any designer to NOT allow the environmental aspect of our company to lead them to design brochures more fitting for Green Tech companies or Alternative Energy.

Target Market(s)

Engineers, Factory Managers, Project Managers, Consultants, Heads of Large Companies, Service Managers

Industry/Entity Type

Industrial

Requirements
Must have
• The brochure must
-Be divided like the services section of our website w/ categories in this order:
-Industrial Services, Waste Management, Remediation Services, Emergency Response, Marine Services, Stormwater Services
-Owing to the large info in these sections, I'd recommend separate pages or tabs
-Incorporate our colors
-Use photos from the site

```html
<!DOCTYPE html>
<html lang="en">
<head>
<meta charset="utf-8">
<title>KVL Terra – Industrial Services &amp; Waste Management</title>
<link rel="stylesheet" href="https://fonts.googleapis.com/css2?family=Carlito:wght@400;700&family=Marcellus&family=Tinos:ital,wght@0,400;1,400;1,700&display=swap">
<style>
  :root{
    --stage:#3a3a3c;
    --page:#1c3a4c;
    --band-light:#4f8199;
    --accent:#f0952a;
    --text:#dbe5eb;
    --rule:#5f8396;
    --quote-bg:#e3e6e8;
    --quote-text:#2b2f33;
    --photo-steel:#6d8aa3;
    --photo-sky:#8fb0cf;
  }
  *{box-sizing:border-box;margin:0;padding:0}
  html,body{width:1200px;height:900px;overflow:hidden;background:var(--stage)}
  body{position:relative;font-family:"Carlito",sans-serif;color:var(--text)}

  .spread{position:absolute;left:44px;top:228px;width:1112px;height:444px;display:flex}
  .page{position:relative;width:556px;height:444px;background:var(--page);overflow:hidden}

  .photo{position:absolute}
  .photo--plant{background:linear-gradient(180deg,var(--photo-sky) 0%,var(--photo-steel) 45%,#2f4a5e 100%)}
  .photo--truck{background:linear-gradient(180deg,#9ec2e2 0%,#c9d2d6 50%,#8b7f63 100%)}
  .photo--hydro{background:linear-gradient(135deg,#3a3a36 0%,#7a7462 50%,#c9b64a 75%,#3f3c35 100%)}
  .photo--suit{background:linear-gradient(135deg,#5b2a1c 0%,#c4582c 50%,#7a3a22 100%)}
  .photo--pipes{background:linear-gradient(180deg,#4b7fae 0%,#8aa7bf 50%,#2d4458 100%)}
  .photo--pour{background:linear-gradient(160deg,#5c6c79 0%,#8f9aa2 35%,#3e4c58 70%,#1d2a33 100%)}
  .photo--drums{background:linear-gradient(180deg,#7a5036 0%,#a2663e 45%,#5a6f7e 75%,#3b3027 100%)}

  .quote{position:absolute;z-index:3;background:var(--quote-bg);border:1px solid #9aa6ae;box-shadow:0 2px 4px rgba(0,0,0,.35);color:var(--quote-text);font-family:"Tinos",serif;font-style:italic;font-size:6.9px;line-height:8.1px;padding:5px 7px 6px}
  .quote__text{text-align:justify}
  .quote__who{margin-top:7px;font-weight:700;font-size:7.4px;line-height:8.4px}
  .quote__org{font-style:italic}

  .band{position:absolute;z-index:1;left:0;width:556px;background:radial-gradient(ellipse 60% 120% at 55% 55%,var(--band-light) 0%,var(--page) 75%)}
  .page--right .band{background:radial-gradient(ellipse 55% 120% at 30% 40%,var(--band-light) 0%,var(--page) 75%)}

  .section-title{position:absolute;z-index:2;font-family:"Marcellus",serif;font-weight:400;color:#fff;font-size:15px;letter-spacing:3.6px;text-transform:uppercase;white-space:nowrap}
  .section-title__initial{font-size:30px;letter-spacing:1px}

  .rule{position:absolute;z-index:2;height:1px;background:var(--rule)}

  .body-copy{position:absolute;font-size:7.6px;line-height:10.4px;color:var(--text)}
  .body-copy p+p{margin-top:9px}
  .body-copy--justified p{text-align:justify}

  .capabilities{position:absolute;left:36px;top:316px;width:484px;display:flex}
  .capability{width:123px;padding-right:8px;border-right:1px solid var(--rule);padding-left:6px}
  .capability:first-child{padding-left:0}
  .capability:last-child{border-right:none}
  .capability h3{font-size:6.6px;font-weight:700;color:#fff;margin-bottom:9px;line-height:8px}
  .capability ul{list-style:none}
  .capability li,.waste-list li{font-size:6.4px;line-height:8.7px;padding-left:6px;position:relative}
  .capability li::before,.waste-list li::before{content:"";position:absolute;left:0;top:3.4px;width:2px;height:2px;background:var(--text);border-radius:50%}

  .waste-heading{font-size:6.6px;font-weight:700;color:#fff;margin:18px 0 10px 6px}
  .waste-list{list-style:none}
  .waste-list li{font-size:6.2px;line-height:8.8px}

  .footer{position:absolute;z-index:2;left:0;top:412px;width:556px;height:32px;background:var(--accent);color:#fff;font-size:7px;display:flex;align-items:center}
  .footer--left{padding-left:36px;word-spacing:1px}
  .footer--right{justify-content:flex-end;padding-right:20px;gap:18px}
  .brand{display:flex;align-items:center;gap:4px;font-weight:700;font-size:9px;letter-spacing:.5px}
  .brand__mark{width:7px;height:7px;background:#fff}
</style>
</head>
<body>
<main class="spread">

  <section class="page page--left">
    <div class="photo photo--plant" style="left:0;top:0;width:556px;height:75px" role="img" aria-label="Photo of industrial plant piping and steel structures"></div>

    <blockquote class="quote" style="left:36px;top:37px;width:190px">
      <div class="quote__text">“I have utilized KVL Terra's services for the past 8 years at two separate industrial manufacturing companies located in North Carolina. They are well trained and professional and when they are on the job at your site they give 100%. I have always been completely satisfied with the service I have gotten from KVL Terra, and have no hesitation whatsoever in highly recommending them for your job, no matter how large or small.”</div>
      <div class="quote__who">-Environmental Manager</div>
      <div class="quote__org">Chemical Manufacturing Plant</div>
    </blockquote>

    <div class="band" style="top:75px;height:66px"></div>
    <h2 class="section-title" style="left:292px;top:92px"><span class="section-title__initial">I</span>ndustrial Services</h2>
    <div class="rule" style="left:34px;top:142px;width:490px"></div>

    <div class="body-copy" style="left:38px;top:148px;width:488px">
      <p>KVL Terra's Industrial Services Division is the hardest working team in the business. We're at work 24 hours a day, 365 days a year in a diverse array of facilities across the Southeast. For over 20 years, we've been safely and efficiently performing all facets of industrial cleaning. With the equipment of a large company and the attention to detail of a small one, KVL Terra gets the job done right the first time, every time. Partnering with us translates to “peace of mind.” No more worrying that the job will be done on time. No more worrying about accidents. No more worrying about hidden fees or the dreaded “change order.” Just your project done right.</p>
      <p>Here's a partial overview of our capabilities:</p>
    </div>

    <div class="photo photo--truck" style="left:36px;top:222px;width:115px;height:80px" role="img" aria-label="Photo of a vacuum truck on site"></div>
    <div class="photo photo--hydro" style="left:159px;top:222px;width:115px;height:80px" role="img" aria-label="Photo of a worker hydro blasting equipment"></div>
    <div class="photo photo--suit" style="left:282px;top:222px;width:115px;height:80px" role="img" aria-label="Photo of a worker in protective suit cleaning a vessel"></div>
    <div class="photo photo--pipes" style="left:405px;top:222px;width:115px;height:80px" role="img" aria-label="Photo of plant piping and yellow railings"></div>

    <div class="capabilities">
      <div class="capability">
        <h3>Vacuum Truck Service</h3>
        <ul>
          <li>Sump/ Pit Cleaning</li>
          <li>Oil-water separator cleaning and maintenance</li>
          <li>Bulk solids and ash handling</li>
          <li>Aggressive Fluid Vapor Recovery</li>
          <li>Liquids vacuum transfer and removal</li>
          <li>Liquids and solids transportation</li>
        </ul>
      </div>
      <div class="capability">
        <h3>Hydro blasting Services</h3>
        <ul>
          <li>No entry (3D tool) tank cleaning</li>
          <li>Interior and Exterior surface cleaning</li>
          <li>Tanks, reactor, and vessel cleaning</li>
          <li>Tube and process pipe “lancing”</li>
          <li>Boilers, ships, barges, and railcars, etc.</li>
          <li>Evaporator and heat exchanger cleaning</li>
          <li>Unclogging drainage lines</li>
        </ul>
      </div>
      <div class="capability">
        <h3>Facility Maintenance and Cleaning Services</h3>
        <ul>
          <li>Tank and Line Cleaning</li>
          <li>Scheduled/ Emergency plant shutdowns</li>
          <li>Cooling towers</li>
          <li>Drain and sump cleanout</li>
          <li>Oil-water separators</li>
          <li>No dig utilities excavation with hydro excavation</li>
        </ul>
      </div>
      <div class="capability">
        <h3>Product Handling</h3>
        <ul>
          <li>Hazardous and Non-Hazardous Material Removal</li>
          <li>Product Transfer</li>
          <li>Solidification</li>
          <li>Stabilization</li>
          <li>Product recovery and recycling</li>
          <li>Wastewater Treatment</li>
          <li>Waste Transportation</li>
        </ul>
      </div>
    </div>

    <footer class="footer footer--left">1870 Harbor Road, Port Langley, NC 28199 &nbsp;•&nbsp; Phone: (555) 014-2270 &nbsp;•&nbsp; Fax: (555) 014-2281</footer>
  </section>

  <section class="page page--right">
    <div class="body-copy body-copy--justified" style="left:35px;top:30px;width:208px">
      <p>KVL Terra provides transportation, recycling, and disposal of all types of hazardous and non-hazardous wastes.</p>
      <p>Our team is able to analyze, categorize, and then handle waste in the safest and most efficient way using the most up-to-date treatment methods. Meanwhile, our recycling program keeps waste out of the landfills and helps turn used oil back into usable product.</p>
      <p>KVL Terra will analyze your waste stream and determine what method of treatment will be most effective and most efficient. Whether it needs to be stabilized, solidified, blended, or treated in our wastewater system, we can come up with a unique solution to help handle your waste.</p>
      <h3 class="waste-heading">Waste categories</h3>
      <ul class="waste-list">
        <li>Liquids, solids, sludges, and residuals</li>
        <li>Hazardous and non-hazardous</li>
        <li>Lab Packs</li>
        <li>Drums</li>
        <li>Totes</li>
        <li>Roll offs</li>
        <li>Byproducts</li>
        <li>Used oil and petroleum products, off spec materials</li>
      </ul>
    </div>

    <div class="photo photo--pour" style="left:249px;top:0;width:275px;height:274px" role="img" aria-label="Photo of a gloved hand pouring waste liquid from a pipe"></div>
    <div class="rule" style="left:0;top:275px;width:524px"></div>

    <div class="band" style="top:276px;height:64px"></div>
    <h2 class="section-title" style="left:33px;top:290px"><span class="section-title__initial">W</span>aste Management</h2>

    <div class="photo photo--drums" style="left:0;top:340px;width:556px;height:72px" role="img" aria-label="Photo of rows of rusty waste drums"></div>

    <blockquote class="quote" style="left:366px;top:296px;width:159px">
      <div class="quote__text">“Their personnel and equipment have helped me complete tasks on time and meet budgets repeatedly. When I have KVL Terra on-site it means I have one less item to be concerned about.”</div>
      <div class="quote__who">-Principal</div>
      <div class="quote__org">Environmental Consulting Group</div>
    </blockquote>

    <footer class="footer footer--right">
      <span>24-HOUR EMERGENCY HOTLINE: (800) 555-0199</span>
      <span class="brand"><span class="brand__mark"></span>KVL TERRA</span>
    </footer>
  </section>

</main>
</body>
</html>
```